General Contractor Marketing Flyer

Need a flyer to hand out at trade show directed towards craft breweries and restaurants. We are a General Contractor that builds projects for industry. We also can provide design services when requested.
We are located in Chicago, IL and work throughout the US. Would like to see a design that emphasizes our expertise and knowledge within the Hospitality industry. We are including our logo and some previous work experience. Our website is www.harbeckbuild.com for further information

```html
<!DOCTYPE html>
<html lang="en">
<head>
<meta charset="utf-8">
<title>Harbeck Build – General Contracting Flyer</title>
<link href="https://fonts.googleapis.com/css2?family=League+Spartan:wght@400;600;700;800&family=Arimo:wght@400;700&family=Oswald:wght@500;600&display=swap" rel="stylesheet">
<style>
  :root{
    --yellow:#f2cd00;
    --yellow-bright:#ffd900;
    --charcoal:#2b2b2b;
    --ink:#333333;
    --grey:#77777a;
    --grey-light:#a8a8a8;
    --white:#ffffff;
    --page:#ffffff;
  }
  *{box-sizing:border-box;margin:0;padding:0}
  html,body{width:1200px;height:1200px;overflow:hidden;background:var(--page)}
  .flyer{position:absolute;left:218px;top:105px;width:765px;height:990px;background:var(--white);overflow:hidden;font-family:'Arimo',Arial,sans-serif}
  .hero-photo{position:absolute;left:0;top:0;width:765px;height:500px;
    background:radial-gradient(ellipse at 55% 40%,#c98a3f 0%,#8a5320 40%,#3a2414 75%,#1e1510 100%)}
  .logo-box{position:absolute;left:31px;top:0;width:178px;height:132px;background:rgba(255,255,255,.9);
    display:flex;align-items:center;justify-content:center}
  .logo-name{font-family:'League Spartan',sans-serif;font-weight:700;font-size:22px;letter-spacing:2px;color:var(--grey);text-transform:uppercase;text-align:center;line-height:1.1}
  .headline-band{position:absolute;left:0;top:352px;width:765px;height:148px}
  .headline{position:absolute;left:31px;top:364px;font-family:'League Spartan',sans-serif;color:var(--ink);line-height:1}
  .headline .l1{font-size:29px;font-weight:400;letter-spacing:-.3px;display:block}
  .headline .l2{font-size:26px;font-weight:800;display:block;margin-top:4px;word-spacing:6px}
  .headline .l3{font-size:45px;font-weight:800;color:var(--white);display:block;margin-top:4px;letter-spacing:-.5px}
  .headline .l4{font-size:20.5px;font-weight:700;display:block;margin-top:4px}
  .accent-bar{position:absolute;left:519px;top:509px}
  .services-panel{position:absolute;left:31px;top:500px;width:353px;height:490px;background:var(--charcoal)}
  .services-title{position:absolute;left:18px;top:40px;font-family:'League Spartan',sans-serif;font-weight:800;font-size:22px;color:var(--white);letter-spacing:.3px}
  .services-title span{color:var(--grey-light)}
  .service{position:absolute;left:18px;width:320px;display:flex;gap:20px}
  .service svg{flex:none;width:30px;height:30px;margin-top:-2px}
  .service h3{font-family:'Arimo',sans-serif;font-weight:700;font-size:13px;color:var(--yellow-bright);margin-bottom:3px}
  .service p{font-size:10px;line-height:1.25;color:#e8e8e8}
  .work-photo{position:absolute;left:421px;width:305px;height:157px;border:4px solid var(--white);box-shadow:0 1px 4px rgba(0,0,0,.35)}
  .work-photo.cafe{top:546px;background:linear-gradient(180deg,#8f959c 0%,#c9cbcc 45%,#6d6a66 100%)}
  .work-photo.bar{top:720px;background:linear-gradient(160deg,#6d5a3c 0%,#4a2d1c 50%,#2a1812 100%)}
  .call-bar{position:absolute;left:0;top:892px;width:409px;height:75px;background:var(--white);box-shadow:0 2px 6px rgba(0,0,0,.3)}
  .call-tab{position:absolute;left:384px;top:880px}
  .call-label{position:absolute;left:31px;top:7px;font-family:'Oswald',sans-serif;font-weight:600;font-size:29px;line-height:1;color:var(--ink)}
  .call-divider{position:absolute;left:155px;top:10px;width:3px;height:56px;background:var(--yellow)}
  .contact-row{position:absolute;left:180px;display:flex;align-items:center;gap:16px;color:var(--ink)}
  .contact-row svg{width:18px;height:18px;flex:none}
  .contact-row .phone{font-weight:700;font-size:23px;letter-spacing:.3px}
  .contact-row .small{font-size:13.5px}
  .location-bar{position:absolute;left:409px;top:905px;width:356px;height:52px;background:var(--grey)}
  .location-bar svg{position:absolute;left:19px;top:9px}
  .company{position:absolute;left:48px;top:9px;font-weight:700;font-size:16.5px;color:var(--yellow-bright);letter-spacing:.3px}
  .city{position:absolute;left:48px;top:30px;font-size:14px;color:var(--white)}
</style>
</head>
<body>
<main class="flyer">
  <div class="hero-photo" role="img" aria-label="Photo of a finished brewery taproom with timber ceiling, hanging bulb lights and long wooden tables"></div>

  <div class="logo-box"><div class="logo-name">Harbeck<br>Build</div></div>

  <svg class="headline-band" viewBox="0 0 765 148" aria-hidden="true">
    <polygon points="0,0 367,0 445,148 0,148" fill="var(--yellow)"/>
    <polygon points="361,14 368,14 433,140 426,140" fill="var(--grey)"/>
    <rect x="451" y="127" width="314" height="9" fill="var(--yellow-bright)"/>
  </svg>

  <h1 class="headline">
    <span class="l1">SERVING ALL OF YOUR</span>
    <span class="l2">GENERAL CONTRACTING</span>
    <span class="l3">CONSTRUCTION</span>
    <span class="l4">MANAGEMENT AND DESIGN NEEDS</span>
  </h1>

  <svg class="accent-bar" width="246" height="20" viewBox="0 0 246 20" aria-hidden="true">
    <polygon points="0,0 246,0 246,20 12,20" fill="var(--yellow-bright)"/>
  </svg>

  <section class="services-panel">
    <h2 class="services-title"><span>OUR</span> SERVICES</h2>

    <div class="service" style="top:84px">
      <svg viewBox="0 0 30 30" fill="none" stroke="var(--yellow)" stroke-width="1.5"><path d="M15 9c-2-4-8-3-7 2 1 3 7 7 7 7s6-4 7-7c1-5-5-6-7-2z"/><path d="M3 12v7l7 6v3M27 12v7l-7 6v3"/><path d="M13 12h4M15 10v4"/></svg>
      <div><h3>Health and Wellness</h3><p>Dental offices, clean rooms, Labs, Procedure rooms, Family Care, rehabilitation facilities, Eye Care</p></div>
    </div>

    <div class="service" style="top:140px">
      <svg viewBox="0 0 30 30" fill="none" stroke="var(--yellow)" stroke-width="1.5"><path d="M10 8a5 5 0 0 1 10 0v3H10z"/><rect x="8" y="11" width="14" height="17"/><rect x="2" y="17" width="6" height="11"/><rect x="22" y="17" width="6" height="11"/><path d="M15 14v6M12 17h6"/></svg>
      <div><h3>Hospitality/Entertainment</h3><p>Hotels, Adventure parks, go cart racing, zipline facilities, Climbing amusement facilities, Country Cubs</p></div>
    </div>

    <div class="service" style="top:203px">
      <svg viewBox="0 0 30 30" fill="none" stroke="var(--yellow)" stroke-width="1.5"><rect x="3" y="3" width="10" height="7"/><circle cx="18" cy="7" r="3"/><rect x="3" y="18" width="18" height="7"/><path d="M5 25v3M19 25v3M26 10v18M23 28h6"/></svg>
      <div><h3>Interiors</h3><p>Corporate office, retail office, building rehabs, Code Compliance Repairs, Collaboration spaces, Schools, Condo building common space</p></div>
    </div>

    <div class="service" style="top:274px">
      <svg viewBox="0 0 30 30" fill="none" stroke="var(--yellow)" stroke-width="1.5"><rect x="5" y="2" width="20" height="6"/><path d="M3 8h24l-2 4H5z"/><rect x="5" y="12" width="20" height="16"/><rect x="12" y="17" width="6" height="11"/></svg>
      <div><h3>Restaurant</h3><p>Breweries, National restaurants, fine dining, Bars, local retail restaurants</p></div>
    </div>

    <div class="service" style="top:333px">
      <svg viewBox="0 0 30 30" fill="none" stroke="var(--yellow)" stroke-width="1.5"><rect x="10" y="2" width="10" height="6"/><path d="M2 8h26v5H2z"/><rect x="3" y="13" width="24" height="15"/><rect x="6" y="18" width="6" height="10"/><rect x="15" y="18" width="9" height="6"/></svg>
      <div><h3>Retail</h3><p>Fashion stores, mall restoration, retail office, national retailers, fitness, health Care, salons</p></div>
    </div>
  </section>

  <div class="work-photo cafe" role="img" aria-label="Photo of a bright industrial cafe interior with globe pendant lights and wooden tables"></div>
  <div class="work-photo bar" role="img" aria-label="Photo of a restaurant bar with wood cabinetry, leather bar stools and wall screens"></div>

  <svg class="call-tab" width="30" height="100" viewBox="0 0 30 100" aria-hidden="true">
    <polygon points="0,0 25,12 0,12" fill="var(--charcoal)"/>
    <polygon points="0,100 25,87 0,87" fill="var(--charcoal)"/>
  </svg>

  <div class="call-bar">
    <div class="call-label">CALL US<br>TODAY</div>
    <div class="call-divider"></div>
    <div class="contact-row" style="top:3px">
      <svg viewBox="0 0 24 24" fill="var(--ink)"><path d="M6.6 10.8a15 15 0 0 0 6.6 6.6l2.2-2.2a1 1 0 0 1 1-.25 11.4 11.4 0 0 0 3.6.6 1 1 0 0 1 1 1V20a1 1 0 0 1-1 1A17 17 0 0 1 3 4a1 1 0 0 1 1-1h3.5a1 1 0 0 1 1 1 11.4 11.4 0 0 0 .6 3.6 1 1 0 0 1-.25 1z"/></svg>
      <span class="phone">708-555-0147</span>
    </div>
    <div class="contact-row" style="top:35px">
      <svg viewBox="0 0 24 24" fill="none" stroke="var(--ink)" stroke-width="1.6"><rect x="3" y="5" width="18" height="14" rx="1"/><path d="M3 6l9 7 9-7M3 18l7-6M21 18l-7-6"/></svg>
      <span class="small">info@harbeckbuild.com</span>
    </div>
    <div class="contact-row" style="top:52px">
      <svg viewBox="0 0 24 24" fill="none" stroke="var(--ink)" stroke-width="1.6"><circle cx="12" cy="12" r="9"/><ellipse cx="12" cy="12" rx="4" ry="9"/><path d="M3 12h18M5 7h14M5 17h14"/></svg>
      <span class="small">www.harbeckbuild.com</span>
    </div>
  </div>

  <div class="location-bar">
    <svg width="14" height="20" viewBox="0 0 14 20"><path d="M7 0a7 7 0 0 0-7 7c0 5 7 13 7 13s7-8 7-13a7 7 0 0 0-7-7zm0 10a3 3 0 1 1 0-6 3 3 0 0 1 0 6z" fill="var(--yellow-bright)"/></svg>
    <div class="company">HARBECK BUILD, INC.</div>
    <div class="city">Chicago,IL</div>
  </div>
</main>
</body>
</html>
```